Flyer für ein Onlineportal für private Vermieter
Design hat direkt unseren Geschmack getroffen.
Zielgruppe
Onlineportal für private Vermieter. Zentrale Botschaft: Mieterhöhungen sind in Orten ohne Mietspiegel fast unmöglich. Die Lösung? Ortsübliche Vergleichsmieten. Unsere Plattform bietet Zugang zu ortsüblichen Vergleichsmieten.
Aufgabenstellung
Stock-Bilder bitte von Velmora Bildarchiv, weil wir hier ein Abonnement haben.

```html
<!DOCTYPE html>
<html lang="de">
<head>
<meta charset="utf-8">
<title>Nachhaltig vermieten – Flyer</title>
<link rel="stylesheet" href="https://fonts.googleapis.com/css2?family=Montserrat:wght@300;700&display=swap">
<style>
  :root {
    --paper: #ffffff;
    --sky: #67baea;
    --ink: #0d0d0d;
  }
  * { margin: 0; padding: 0; box-sizing: border-box; }
  html, body { width: 846px; height: 1200px; overflow: hidden; background: var(--paper); }
  .flyer { position: relative; width: 846px; height: 1200px; background: var(--paper); overflow: hidden; }

  .band { position: absolute; left: 640px; top: 0; width: 147px; height: 1200px; background: var(--sky); }
  .edge { position: absolute; left: 807px; width: 39px; background: var(--ink); }
  .edge--top { top: 0; height: 605px; }
  .edge--bottom { top: 629px; height: 571px; }

  .vertical {
    position: absolute;
    bottom: 76px;
    writing-mode: vertical-rl;
    transform: rotate(180deg);
    color: var(--paper);
    font-family: "Montserrat", sans-serif;
    line-height: 1;
    white-space: nowrap;
  }
  .headline { left: 657px; font-size: 76px; font-weight: 700; letter-spacing: 2.4px; }
  .subline { left: 734px; font-size: 42px; font-weight: 300; letter-spacing: 1px; }

  .brand {
    position: absolute;
    left: 78px;
    top: 1062px;
    font-family: "Montserrat", sans-serif;
    font-weight: 700;
    font-size: 34px;
    letter-spacing: 1px;
    color: var(--ink);
  }
</style>
</head>
<body>
  <main class="flyer">
    <div class="band"></div>
    <div class="edge edge--top"></div>
    <div class="edge edge--bottom"></div>

    <h1 class="vertical headline">NACHHALTIG VERMIETEN</h1>
    <p class="vertical subline">PRIVATVERMIETER SIND KEINE MIETKONZERNE.</p>

    <p class="brand">WOHNKREIS</p>
  </main>
</body>
</html>
```